Glimmerfold School Blast & Email Marketing

Create and eblast that can be sent through constant contacts and other email distibution

Target Market(s)

Schools and educational organizations

Industry/Entity Type

Museum

Font styles to use
Sans Serif

Colors
e667a6
ffffff

Requirements
Must have
• Black, pink & white color scheme; graphics to separate content for easy reading; photos; appealing imagery and design; museum logo, address, website and phone number; editable final version; incorporate the exhibit, Glimmerfold, elements; compatible and aligned with Constant Contact requirements for distribution.

```html
<!DOCTYPE html>
<html lang="en">
<head>
<meta charset="utf-8">
<title>Glimmerfold Activities</title>
<link rel="stylesheet" href="https://fonts.googleapis.com/css2?family=Arimo:wght@700&family=Roboto:wght@400&display=swap">
<style>
  :root {
    --accent-blue: #00a9e8;
    --panel-grey: #f6f6f6;
    --page-white: #ffffff;
    --ring-pink: #e8319a;
    --heading-pink: #e6409e;
    --ink: #111111;
  }
  * { margin: 0; padding: 0; box-sizing: border-box; }
  html, body {
    width: 749px;
    height: 1200px;
    overflow: hidden;
    background: var(--page-white);
  }
  .eblast {
    position: relative;
    width: 749px;
    height: 1200px;
    background: var(--page-white);
  }
  .top-band {
    position: absolute;
    left: 29px; top: 0;
    width: 702px; height: 9px;
    background: var(--accent-blue);
  }
  .activities-panel {
    position: absolute;
    left: 29px; top: 21px;
    width: 702px; height: 1155px;
    background: var(--panel-grey);
  }
  .section-title {
    position: absolute;
    left: 0; top: 50px;
    width: 100%;
    text-align: center;
    font-family: "Arimo", Arial, sans-serif;
    font-weight: 700;
    font-size: 35px;
    letter-spacing: 0.5px;
    color: var(--ink);
  }
  .activity {
    position: absolute;
    width: 320px;
    text-align: center;
  }
  .activity--left { left: 12px; }
  .activity--right { left: 356px; }
  .activity--row1 { top: 149px; }
  .activity--row2 { top: 634px; }
  .activity-photo {
    width: 246px; height: 246px;
    margin: 0 auto;
    border-radius: 50%;
    border: 9px solid var(--ring-pink);
    background-clip: padding-box;
    box-shadow: inset 0 0 0 5px var(--page-white);
  }
  .photo-theater { background-image: radial-gradient(circle at 50% 45%, #b84a3a 0%, #4a3630 45%, #1e1a1a 100%); }
  .photo-dissection { background-image: linear-gradient(135deg, #dfe7ee 0%, #7fa0c8 45%, #3656a8 75%, #a67a62 100%); }
  .photo-recycle { background-image: radial-gradient(circle at 50% 40%, #6fbf3a 0%, #3f8a2a 35%, #2a2a2a 70%, #050505 100%); }
  .photo-auscultation { background-image: linear-gradient(120deg, #5c6068 0%, #c8a48c 50%, #e7c2a6 75%, #8a8f96 100%); }
  .activity-name {
    font-family: "Arimo", Arial, sans-serif;
    font-weight: 700;
    font-size: 20px;
    line-height: 25px;
    color: var(--heading-pink);
    text-transform: uppercase;
  }
  .activity--row1 .activity-name { margin-top: 32px; }
  .activity--row2 .activity-name { margin-top: 27px; }
  .activity--row2.activity--right .activity-name { margin-top: 30px; }
  .activity-copy {
    font-family: "Roboto", Arial, sans-serif;
    font-size: 16px;
    line-height: 26px;
    color: var(--ink);
    margin: 18px auto 0;
    width: 300px;
  }
  .activity--row1 .activity-copy { margin-top: 18px; }
  .activity--row2.activity--left .activity-copy { margin-top: 14px; }
  .activity--row2.activity--right .activity-copy { margin-top: 40px; }
</style>
</head>
<body>
  <div class="eblast">
    <div class="top-band"></div>
    <section class="activities-panel">
      <h1 class="section-title">ACTIVITIES</h1>

      <article class="activity activity--left activity--row1">
        <div class="activity-photo photo-theater" role="img" aria-label="Photo of the lit marquee sign of the Halvorsen Theater"></div>
        <h2 class="activity-name">Halvorsen Theater</h2>
        <p class="activity-copy">Sonic Magic</p>
      </article>

      <article class="activity activity--right activity--row1">
        <div class="activity-photo photo-dissection" role="img" aria-label="Photo of a science educator in protective gear performing a dissection"></div>
        <h2 class="activity-name">Live Dissection Demos</h2>
        <p class="activity-copy">Take a seat inside the Halvorsen theater and follow a live dissection of a cow eye or a sheep brain performed by one of the museum science educators.</p>
      </article>

      <article class="activity activity--left activity--row2">
        <div class="activity-photo photo-recycle" role="img" aria-label="Photo of recycled cans and jars with fresh grass growing from them"></div>
        <h2 class="activity-name">Engineering Design<br>Station: Musical<br>Discovery</h2>
        <p class="activity-copy">Design musical instruments from scratch using recyclable materials and what you can find at home.</p>
      </article>

      <article class="activity activity--right activity--row2">
        <div class="activity-photo photo-auscultation" role="img" aria-label="Photo of a student listening to a training mannequin with a stethoscope"></div>
        <h2 class="activity-name">Auscultation</h2>
        <p class="activity-copy">Listening to the sounds of the body. Listen to your own internal music and learn about the instruments that allows doctors to listen to your body.</p>
      </article>
    </section>
  </div>
</body>
</html>
```